Corvane Building Company Portfolio Design

I need a full design for a Company Portfolio for a Kuwait based company called Corvane Building Company, WLL. We offer services in Construction ( Supply of Construction Machinery & Construction Material), Contracting (Steel Structure, Furnishing & Finishing) and Smart Solutions (Smart Homes & Smart Parking).

https://www.filtrobay.com/s/qmtpvkadnehzwro/Photos.zip
Updates

This is a Filtro Bay Link containing all our images that can be used in the Company Profile.

One or more of each can be more than enough to describe each product or service we provide.

Target Market(s)

Construction Companies, Engineering & Design Companies, Consultancy firms.

Industry/Entity Type

Construction

Requirements
Must have
• 1) Must allow for further addition & modification.
Nice to have
• 1) External Photos can be used for a better look & resolution.

```html
<!DOCTYPE html>
<html lang="en">
<head>
<meta charset="utf-8">
<title>Corvane Building Company – Smart Solutions</title>
<link href="https://fonts.googleapis.com/css2?family=Open+Sans:wght@400;700&family=Saira+Condensed:wght@700&family=Saira+Extra+Condensed:wght@300;400&display=swap" rel="stylesheet">
<style>
  :root{
    --teal:#0e7a80;
    --black:#000;
    --white:#fff;
    --ink:#111;
    --rule:#9a9a9a;
  }
  *{margin:0;padding:0;box-sizing:border-box}
  html,body{width:1200px;height:943px;overflow:hidden;background:var(--white)}
  .page{position:relative;width:1200px;height:943px;font-family:"Open Sans",Arial,sans-serif}
  .block{position:absolute}
  .side-band{left:0;top:8px;width:174px;height:847px;background:var(--teal)}
  .side-foot{left:0;top:862px;width:174px;height:48px;background:var(--teal)}
  .side-rule{left:181px;top:8px;width:5px;height:902px;background:var(--teal)}
  .main-panel{left:186px;top:285px;width:587px;height:570px;background:var(--teal)}
  .main-foot{left:186px;top:862px;width:587px;height:48px;background:var(--teal)}
  .title-bar{left:186px;top:214px;width:587px;height:6px;background:var(--teal)}
  .foot-rule{left:0;top:910px;width:130px;height:1px;background:var(--rule)}
  .foot-tick{left:33px;top:918px;width:1px;height:25px;background:var(--rule)}

  .brand{position:absolute;left:253px;top:66px;display:flex;align-items:center;gap:16px}
  .brand-name{font-family:"Saira Condensed",sans-serif;font-weight:700;color:var(--ink);line-height:1}
  .brand-name .big{display:block;font-size:48px;letter-spacing:1px}
  .brand-name .small{display:block;font-size:13px;letter-spacing:4.6px;margin-top:4px}
  .brand-mark{width:26px;height:26px;background:var(--teal)}

  .section-title{position:absolute;left:210px;top:172px;font-family:"Saira Condensed",sans-serif;font-weight:700;font-size:36px;letter-spacing:7px;color:var(--teal);line-height:1;white-space:nowrap}

  .intro{position:absolute;left:200px;top:224px;overflow:visible}
  .intro text{font-family:"Open Sans",Arial,sans-serif;font-weight:700;font-size:13px;fill:var(--teal)}

  .heading-thin{position:absolute;overflow:visible}
  .heading-thin text{font-family:"Saira Extra Condensed",sans-serif;font-weight:300;fill:var(--white)}
  .homes-title{left:192px;top:300px}
  .parking-title{left:806px;top:62px}

  .homes-copy{position:absolute;left:193px;top:354px;width:565px;font-size:11.4px;line-height:13.7px;color:var(--white)}
  .homes-photo{position:absolute;left:247px;top:582px;width:434px;height:246px;background:linear-gradient(135deg,#f2f2f2 0%,#cfcfcf 45%,#5a5a5a 80%,#2a2a2a 100%)}

  .parking-panel{left:773px;top:47px;width:413px;height:808px;background:var(--black)}
  .parking-foot{left:773px;top:862px;width:413px;height:50px;background:var(--black)}
  .parking-rule{position:absolute;left:785px;top:114px;width:401px;height:3px;background:var(--white)}
  .parking-photo{position:absolute;left:823px;top:131px;width:330px;height:205px;background:linear-gradient(180deg,#cfe0ee 0%,#8fa6c4 45%,#4d6aa8 70%,#bfbfbf 100%)}
  .parking-diagram{position:absolute;left:825px;top:348px;width:328px;height:172px;background:linear-gradient(90deg,#e9e9e9 0%,#d8d8d8 50%,#e4e4e4 100%)}
  .parking-copy{position:absolute;left:782px;top:537px;width:402px;font-size:11.4px;line-height:13.7px;color:var(--white)}
  .parking-copy p+p{margin-top:13.7px}
</style>
</head>
<body>
<div class="page">
  <div class="block side-band"></div>
  <div class="block side-foot"></div>
  <div class="block side-rule"></div>
  <div class="block title-bar"></div>
  <div class="block main-panel"></div>
  <div class="block main-foot"></div>
  <div class="block foot-rule"></div>
  <div class="block foot-tick"></div>

  <div class="brand">
    <div class="brand-name"><span class="big">CORVANE</span><span class="small">BUILDING COMPANY</span></div>
    <div class="brand-mark"></div>
  </div>

  <h1 class="section-title">SMART SOLUTIONS</h1>

  <svg class="intro" width="570" height="54" viewBox="0 0 570 54" aria-label="We at Corvane Building Co. have highlighted the need of Smart Solutions to be integrated into our daily lives. Our newly established Smart Solutions Division focuses on two main fields, Smart Homes and Smart Parking.">
    <text x="0" y="12" textLength="562" lengthAdjust="spacing">We at Corvane Building Co. have highlighted the need of Smart Solutions</text>
    <text x="0" y="30" textLength="559" lengthAdjust="spacing">to be integrated into our daily lives. Our newly established Smart Solutions</text>
    <text x="0" y="47" textLength="510" lengthAdjust="spacing">Division focuses on two main fields, Smart Homes and Smart Parking.</text>
  </svg>

  <svg class="heading-thin homes-title" width="192" height="48" viewBox="0 0 192 48" aria-label="Smart Homes">
    <text x="0" y="42" font-size="46" textLength="186" lengthAdjust="spacingAndGlyphs">SMART HOMES</text>
  </svg>
  <p class="homes-copy">Home automation is the residential extension of building automation. It is automation of the home, housework or household activity. Home automation may include centralized control of lighting, HVAC (heating, ventilation and air conditioning), appliances, security locks of gates and doors and other systems, to provide improved convenience, comfort, energy efficiency and security. The popularity of home automation has been increasing greatly in recent years due to much higher affordability and simplicity though smartphone and tablet connectivity. The concept of the "Internet of Things" has tied in closely with the popularization of home automation. A home automation system integrates electrical devices in a house with each other. The techniques employed in home automation include those in building automation as well as the control of domestic activities, such as home entertainment systems, houseplant and yard watering, pet feeding, changing the ambiance "scenes" for different events (such as dinners or parties). Devices may be connected through a computer network to allow control by a personal computer, and may allow remote access from the internet via your Smart Phone. Through the integration of information technologies with the home environment, systems and appliances are able to communicate in an integrated manner, which results in convenience, energy efficiency, and safety benefits as well as a luxurious fully automated home where everything is controllable by a press of a button.</p>
  <div class="homes-photo" role="img" aria-label="Modern living room with a hand holding a smartphone controlling blinds, TV and lights"></div>

  <div class="block parking-panel"></div>
  <div class="block parking-foot"></div>
  <svg class="heading-thin parking-title" width="215" height="46" viewBox="0 0 215 46" aria-label="Smart Parking">
    <text x="0" y="39" font-size="44" textLength="209" lengthAdjust="spacingAndGlyphs">SMART PARKING</text>
  </svg>
  <div class="parking-rule"></div>
  <div class="parking-photo" role="img" aria-label="Cutaway view of a multi-level automated parking garage with stacked cars"></div>
  <div class="parking-diagram" role="img" aria-label="Technical drawings of an automated parking lift system in side and front view"></div>
  <div class="parking-copy">
    <p>A Smart Parking System also known as Automated Parking System (APS) is a mechanical system designed to minimize the area and/or volume required for parking cars. Like a multi-story parking garage, an APS provides parking for cars on multiple levels stacked vertically to maximize the number of parking spaces while minimizing land usage. The APS, however, utilizes a mechanical system to transport cars to and from parking spaces (rather than the driver) in order to eliminate much of the space wasted in a multi-story parking garage. While a multi-story parking garage is similar to multiple parking lots stacked vertically, an APS is more similar to an automated storage and retrieval system for cars.</p>
    <p>With the growing increase of cars in the State of Kuwait, Car drivers are finding it tougher and tougher to find a parking spot, which in-turn leads to traffic chaos. Smart Parking offer a reliable, quick and cost efficient solution to the daily problems faced by car owners whether it be in the industrial, commercial or residential sectors.</p>
    <p>Studies have estimated that on a daily basis 30% of vehicles on the road in the downtown area of major cities are cruising for a parking spot and it takes an average of 7.8 minutes to find one. In addition to aggravation and the waste of time and fuel for drivers looking for parking, this also contributes to additional waste of time and fuel for other drivers as a result of traffic congestion</p>
  </div>
</div>
</body>
</html>
```